Give my personal webpage more appeal!

I need my CV website improved - drmaraloftin.com.au.
I am using the template KESTIN from plovaworks. i would like to keep the already existing theme but am open to suggestions.
Please focus on imagery, colour scheme, and textures to enhance the appeal and look of the page.
The content is there, but now I need a designer to improve the look of my page.
I need styling, royalty-free unique modern images to make the page professional, personal and friendly.
I work in healthcare, so I'm a people person.
I teach professionals and I treat a lot of families.

Target Market(s)

Parents, Professional Healthcare providers

Number of Pages Required

1 page

Font styles to use
Serif
Sans Serif

Requirements
Must have
• My face - image at the top, all the information already contained in it.
• Links to the websites I manage such as my blog.
• One Page website.
• All the information it already contains with the ability to have more.
• Ideally, we would keep the same format for the page although I'm happy to expand column and change the page's structure with in the theme template KESTIN.
Nice to have
• The current KESTIN template. I would like to keep the already existing theme but am open to suggestions.
Should not have
• Multiple pages.

```html
<!DOCTYPE html>
<html lang="en">
<head>
<meta charset="utf-8">
<title>Dr Mara Loftin – Chiropractor</title>
<link rel="stylesheet" href="https://fonts.googleapis.com/css2?family=Raleway:wght@300;400;500&display=swap">
<style>
  :root {
    --ink: #3a3a3a;
    --muted: #555;
    --grey: #7a7a7a;
    --dark: #2f2f2f;
    --brick: #b05446;
    --gold: #e9a41f;
    --white: #ffffff;
    --leaf-a: #4f6b21;
    --leaf-b: #c7c33a;
  }
  * { box-sizing: border-box; margin: 0; padding: 0; }
  html, body { width: 802px; height: 1200px; overflow: hidden; }
  body {
    position: relative;
    background: var(--white);
    font-family: "Raleway", Arial, sans-serif;
    color: var(--ink);
  }
  .abs { position: absolute; }

  /* Header */
  .brand { left: 64px; top: 18px; font-size: 38px; font-weight: 400; color: var(--gold); letter-spacing: 0.5px; }
  .brand-rule { left: 64px; top: 78px; width: 160px; height: 2px; background: var(--grey); }
  .brand-role { left: 228px; top: 72px; font-size: 11px; letter-spacing: 0.5px; color: var(--grey); font-weight: 500; }

  /* About */
  .about { left: 0; top: 90px; width: 802px; height: 252px; background: var(--dark); }
  .leaf-strip { left: 0; top: 342px; width: 802px; height: 10px;
    background: linear-gradient(90deg, var(--leaf-a), var(--leaf-b) 40%, #8aa338 70%, var(--leaf-b)); }
  .portrait { left: 100px; top: 117px; width: 198px; height: 198px; border-radius: 50%;
    background: radial-gradient(circle at 50% 45%, #e8b49a 0 28%, #8a3a2a 29% 40%, #6f9a3a 41%, #3f6a22 100%); }
  .about-title { left: 400px; top: 114px; font-size: 15px; color: var(--white); font-weight: 400; letter-spacing: 0.5px; }
  .about-text { left: 434px; top: 140px; width: 266px; font-size: 8px; line-height: 14px; color: #e6e6e6; font-weight: 300; }
  .about-text p + p { margin-top: 14px; }
  .circle-btn { width: 47px; height: 47px; border-radius: 50%; background: var(--brick);
    color: #f3dcd7; font-size: 6.5px; letter-spacing: 0.3px; display: flex; align-items: center; justify-content: center; top: 279px; }
  .circle-btn.outline { background: transparent; border: 1.5px solid var(--brick); color: var(--brick); }

  /* Tabs */
  .tabs { left: 92px; top: 364px; width: 618px; height: 38px; border-bottom: 1.5px solid var(--brick); display: flex; }
  .tab { width: 157px; display: flex; align-items: center; justify-content: center; text-align: center;
    font-size: 14px; line-height: 17px; color: var(--ink); font-weight: 400; }
  .tab.active { background: var(--brick); color: var(--white); width: 132px; margin-left: 14px; }

  /* Columns */
  .col { top: 424px; width: 132px; }
  .col h3 { font-size: 12.5px; font-weight: 400; line-height: 16px; color: var(--ink); }
  .col .role { font-size: 7.2px; letter-spacing: 0.3px; color: var(--muted); margin-top: 5px; line-height: 10.5px; text-transform: uppercase; }
  .col p { font-size: 7px; line-height: 14px; color: var(--muted); margin-top: 10px; }
  .col p + p { margin-top: 21px; }

  /* Contact */
  .contact { left: 0; top: 732px; width: 802px; height: 250px; background: var(--brick); }
  .contact h2 { position: absolute; left: 218px; top: 14px; font-size: 17px; font-weight: 300; color: var(--white); letter-spacing: 0.5px; }
  .field { left: 218px; width: 365px; height: 28px; background: var(--white); font-size: 7.5px; color: #aaa;
    letter-spacing: 0.5px; padding: 10px 20px; }
  .field.message { height: 42px; }
  .submit { left: 218px; top: 223px; width: 52px; height: 18px; border: 1.5px solid var(--white);
    color: var(--white); font-size: 9.5px; font-weight: 500; display: flex; align-items: center; justify-content: center; }

  /* Partners & footer */
  .partner { top: 1000px; width: 66px; height: 66px; }
  .partner.one { left: 218px; background: var(--white); border: 2px solid #1d1d1d; border-radius: 50%; }
  .partner.two { left: 367px; background: #1d1d1d; }
  .partner.three { left: 517px; background: #111; border-radius: 8px; }
  .foot-brand { left: 0; width: 802px; top: 1098px; text-align: center; font-size: 15px; color: var(--gold); }
  .foot-rule { left: 352px; top: 1121px; width: 98px; height: 1px; background: var(--grey); }
  .social { top: 1143px; font-size: 9px; color: var(--ink); font-weight: 500; }
  .copyright { left: 0; width: 802px; top: 1176px; text-align: center; font-size: 7.5px; letter-spacing: 0.5px; color: var(--ink); }
</style>
</head>
<body>
  <div class="abs brand">dr Mara Loftin</div>
  <div class="abs brand-rule"></div>
  <div class="abs brand-role">CHIROPRACTOR</div>

  <section class="abs about"></section>
  <div class="abs portrait" role="img" aria-label="Portrait photograph of Dr Mara Loftin against green foliage"></div>
  <h1 class="abs about-title">About&nbsp; Me</h1>
  <div class="abs about-text">
    <p>Hello, I am a Chiropractor and a Diplomate of the International Academy of Applied Kinesiology (IAAK). I am also on the board of certified teachers for the IAAK. Teaching engagements take me to local, national and international destinations. Thank you for visiting my page. I look forward to sharing some of my insights with you via my blog.</p>
    <p>I am born and bred here in Brisbane, Australia and love this city that I call home.</p>
  </div>
  <div class="abs circle-btn" style="left:433px">BLOG</div>
  <div class="abs circle-btn" style="left:544px">WEBSITES</div>
  <div class="abs circle-btn outline" style="left:655px">CONTACT</div>
  <div class="abs leaf-strip" role="img" aria-label="Soft green leaf texture band"></div>

  <nav class="abs tabs">
    <div class="tab">Skills</div>
    <div class="tab">Professional<br>Experience</div>
    <div class="tab">Education</div>
    <div class="tab active">Employment</div>
  </nav>

  <article class="abs col" style="left:100px">
    <h3>Kindred Spine Works</h3>
    <div class="role">Founder, Chiropractor</div>
    <p>What a wonderful place to work! I can't come to this clinic and not feel happy. It's decorated for the hundreds of children who get treated here. I've been privileged to watch so many families blossoms through the stages of infancy to teens. They feel like family.</p>
    <p>My job here as Chiropractor has been to train my Chiropractic Associates, Chiropractic Assistants and support staff. To keep the standards high, the team managed and motivated, and the clinic excelling. In July 2016 I sold this business but I continue to work here as an Associate Chiropractor.</p>
  </article>
  <article class="abs col" style="left:257px">
    <h3>Harbourside Spine and Health Centre</h3>
    <div class="role">Associate Chiropractor</div>
    <p>I learned a lot from my mentor Dr Miles Carrow here. He taught me how to think like a business woman, which was exactly what I needed for my next move.</p>
  </article>
  <article class="abs col" style="left:414px">
    <h3>Brightwell Balance Centre</h3>
    <div class="role">Associate Chiropractor</div>
    <p>Working under Dr Roland Avery has been the greatest gift I could have imagined first year out of University. He taught me his life's learnings and I have treasured them. He taught me that the greatest gift for any teacher is to have their student surpass them. He taught me how to be an ego free teacher, share my knowledge unreservedly with those who ask, and how to life without expectations. He shaped me into the practitioner and teacher I have become.</p>
  </article>
  <article class="abs col" style="left:571px">
    <h3>Eastgate University</h3>
    <div class="role">Chiropractor Skills Tutor and Examiner</div>
    <p>What an honour to be invited to tutor and examine 2nd year Chiropractic Skills whilst in my final year of my Masters of Chiropractic. And what a delightful bunch of students we had that year too!</p>
  </article>

  <section class="abs contact">
    <h2>CONTACT</h2>
  </section>
  <div class="abs field" style="top:779px">* YOUR NAME</div>
  <div class="abs field" style="top:820px">* YOUR E-MAIL</div>
  <div class="abs field" style="top:861px">YOUR PHONE NUMBER</div>
  <div class="abs field message" style="top:902px">YOUR MESSAGE</div>
  <div class="abs submit" style="top:955px">SUBMIT</div>

  <div class="abs partner one" role="img" aria-label="Partner badge"></div>
  <div class="abs partner two" role="img" aria-label="Partner badge"></div>
  <div class="abs partner three" role="img" aria-label="Partner badge"></div>

  <div class="abs foot-brand">dr Mara Loftin</div>
  <div class="abs foot-rule"></div>
  <div class="abs social" style="left:352px">Profile</div>
  <div class="abs social" style="left:410px">Network</div>
  <div class="abs copyright">© 2017 DR MARA LOFTIN</div>
</body>
</html>
```